book cover

this is a book titled "the silver compass" it has stories from real people about how they made their dreams come true, have overcome problems .... they use "to think is to create" meaning if you reallly want something you have to picture it in your mind and think on that. kind of like a vision board

```html
<!DOCTYPE html>
<html lang="en">
<head>
<meta charset="utf-8">
<title>The Silver Compass – Book Cover</title>
<link rel="stylesheet" href="https://fonts.googleapis.com/css2?family=Alegreya:wght@400&family=Marcellus&family=Pinyon+Script&display=swap">
<style>
  :root {
    --stage: #d6d6d6;
    --cream: #fcf6cf;
    --ink: #1c1309;
    --script: #fffdf4;
    --art-gold: #d9a03c;
    --art-amber: #a8641a;
    --art-brown: #4a2a0e;
    --art-dark: #120a04;
  }
  html, body {
    margin: 0;
    width: 933px;
    height: 1200px;
    overflow: hidden;
    background: var(--stage);
  }
  .book-cover {
    position: absolute;
    left: 116px;
    top: 73px;
    width: 700px;
    height: 1054px;
    overflow: hidden;
    box-shadow: 0 6px 22px rgba(0,0,0,0.35);
  }
  .cover-art {
    position: absolute;
    inset: 0;
    background: linear-gradient(180deg, var(--art-gold) 0%, var(--art-amber) 45%, var(--art-brown) 65%, var(--art-dark) 85%);
  }
  .cover-band {
    position: absolute;
    left: 0;
    top: 0;
    width: 700px;
    height: 1054px;
  }
  .tagline {
    position: absolute;
    left: 0;
    width: 100%;
    margin: 0;
    text-align: center;
    font-family: "Alegreya", Georgia, serif;
    font-size: 26px;
    line-height: 1;
    color: var(--ink);
  }
  .tagline--top { top: 33px; }
  .tagline--bottom { top: 994px; }
  .title {
    position: absolute;
    inset: 0;
    margin: 0;
    font-weight: 400;
  }
  .title__script {
    position: absolute;
    left: 410px;
    top: 238px;
    font-family: "Pinyon Script", cursive;
    font-size: 88px;
    line-height: 1;
    color: var(--script);
    text-shadow: 0 1px 3px rgba(60,30,0,0.35);
  }
  .title__main {
    position: absolute;
    left: 0;
    top: 322px;
    width: 100%;
    text-align: center;
    font-family: "Marcellus", "Times New Roman", serif;
    font-size: 58px;
    line-height: 1;
    color: var(--ink);
  }
</style>
</head>
<body>
  <main class="book-cover">
    <div class="cover-art" role="img" aria-label="Photograph of golden sunlit clouds fading into dark cloud banks"></div>

    <svg class="cover-band" viewBox="0 0 700 1054" aria-hidden="true">
      <path d="M0 930 C 200 958, 420 972, 560 948 C 640 934, 680 920, 700 912 L700 1054 L0 1054 Z" fill="var(--cream)"/>
    </svg>

    <p class="tagline tagline--top">~ picture it in your mind ~</p>

    <h1 class="title">
      <span class="title__script">The</span>
      <span class="title__main">SILVER COMPASS</span>
    </h1>

    <p class="tagline tagline--bottom">~ to think is to create ~</p>
  </main>
</body>
</html>
```